Bref créative
Quiet Harbor Dental Urgent Clinic- Business Cards and Stationary
Quiet Harbor Dental Urgent Clinic
Professional
Peter Delacroix, Jr., DMD
Founder/ CEO
2718 Pellam Rd
Ste 412
Houston, TX 77291
1-855-GRIN-WELLS
petedx4@mailvane.example
www.GRINWELLS.example
we can see you now!
RED, WHITE AND BLUE
I Have raised the $$$$ for postcard fabrication as well. let's get it!
attached is the graphic concept i'd like to achieve with the postcard.

```html
<!DOCTYPE html>
<html lang="en">
<head>
<meta charset="utf-8">
<title>Quiet Harbor Dental Urgent Clinic – Postcard</title>
<link rel="stylesheet" href="https://fonts.googleapis.com/css2?family=Cinzel:wght@400;700&family=Lato:wght@400;700&display=swap">
<style>
  :root {
    --page: #ffffff;
    --navy: #1d2a4a;
    --red: #c8262e;
    --blue: #2b4f8f;
    --grey: #7a7f88;
    --card-edge: #e3e6ea;
    --photo-light: #eef3f8;
    --photo-mid: #9fb7d3;
    --photo-deep: #2f5d9a;
  }
  * { margin: 0; padding: 0; box-sizing: border-box; }
  html, body {
    width: 1200px; height: 422px; overflow: hidden;
    background: var(--page);
  }
  .canvas { position: relative; width: 1200px; height: 422px; }

  .postcard {
    position: absolute; top: 19px; width: 562px; height: 389px;
    border: 1px solid var(--card-edge);
    box-shadow: 0 2px 6px rgba(0,0,0,0.12);
    overflow: hidden;
  }
  .postcard--front { left: 12px; }
  .postcard--back { left: 619px; background: #fff; }

  .front-photo {
    position: absolute; inset: 0;
    background:
      radial-gradient(ellipse at 40% 45%, var(--photo-light) 0%, rgba(238,243,248,0) 55%),
      linear-gradient(160deg, var(--photo-mid) 0%, var(--photo-light) 45%, var(--photo-deep) 100%);
  }
  .headline {
    position: absolute; left: 130px; top: 282px;
    font-family: "Cinzel", serif; color: var(--navy);
    line-height: 1.05; text-align: left;
  }
  .headline__line { display: block; font-size: 27px; font-weight: 700; letter-spacing: 0.5px; }
  .headline__accent { color: var(--red); }
  .headline__small { font-size: 20px; }

  .brand {
    position: absolute; left: 0; right: 0; top: 158px;
    display: flex; align-items: center; justify-content: center; gap: 12px;
  }
  .brand__mark { width: 46px; height: 46px; border-radius: 50%; background: var(--blue); flex: none; }
  .brand__text { display: flex; flex-direction: column; }
  .brand__name {
    font-family: "Lato", sans-serif; font-weight: 700; font-size: 17px;
    color: var(--navy); letter-spacing: 0.5px; text-transform: uppercase; line-height: 1.2;
    max-width: 220px;
  }
  .brand__tagline {
    font-family: "Lato", sans-serif; font-size: 9px; color: var(--red);
    letter-spacing: 1px; text-transform: uppercase; margin-top: 4px;
  }
  .contact {
    position: absolute; left: 0; right: 0; top: 333px;
    text-align: center; font-family: "Lato", sans-serif;
    font-size: 11px; color: var(--grey); letter-spacing: 2px; line-height: 22px;
  }
</style>
</head>
<body>
<main class="canvas">
  <section class="postcard postcard--front">
    <div class="front-photo" role="img" aria-label="Photo of a toothbrush, dental floss and toothpaste tube on a soft blue background"></div>
    <h1 class="headline">
      <span class="headline__line">A R<span class="headline__accent">EVO</span>LUTIONARY</span>
      <span class="headline__line">APPROACH</span>
      <span class="headline__line headline__small">TOTHESAME OF</span>
      <span class="headline__line"><span class="headline__accent">TOOTH</span> ache</span>
    </h1>
  </section>

  <section class="postcard postcard--back">
    <div class="brand">
      <span class="brand__mark"></span>
      <div class="brand__text">
        <span class="brand__name">Quiet Harbor Dental Urgent Clinic</span>
        <span class="brand__tagline">We can see you now!</span>
      </div>
    </div>
    <div class="contact">
      <p>1-855-GRIN-WELLS</p>
      <p>www.GRINWELLS.example</p>
    </div>
  </section>
</main>
</body>
</html>
```